Vemtra Group: Business Card for a high end technology company

We need a cool new design for our business cards using our cloud logo. We are a technology consulting business. We pride ourselves on be the best of the best. We mainly focus on cloud solutions and managed services. We need a business card that sets us apart from the other technology companies in the area and allows us to stand out.

Target Market(s)

Technology departments, CIO, CEOs, and Information Technology Staff.

Industry/Entity Type

Information Technology

Contact Information for Business Card

Must have the logo and our name.
Must have employee name, email address, office phone, cell phone and website.
Need to have all info on one side a cool design on backside.

Font styles to use
Serif
Sans Serif

Requirements
Must have
• Must have the logo and our name.
• Must have employee name, email address, office phone, cell phone and website.
• Need to have all info on one side a cool design on back side.
• Must be a crisp clean design, not too busy or confusing.

```html
<!DOCTYPE html>
<html lang="en">
<head>
<meta charset="utf-8">
<title>Vemtra Group – Business Card</title>
<link rel="stylesheet" href="https://fonts.googleapis.com/css2?family=Questrial&family=Open+Sans:wght@400;700&display=swap">
<style>
  :root {
    --backdrop: #2f3d44;
    --card-dark: #3b3b3e;
    --card-white: #ffffff;
    --brand-blue: #3a72d0;
    --brand-blue-light: #5f95e6;
    --ink: #2c2c2e;
    --paper-text: #f2f2f2;
  }
  * { box-sizing: border-box; margin: 0; padding: 0; }
  html, body { width: 1200px; height: 900px; overflow: hidden; }
  body {
    background: var(--backdrop);
    font-family: "Open Sans", Arial, sans-serif;
    position: relative;
  }
  .card {
    position: absolute;
    left: 320px;
    width: 560px;
    height: 320px;
    overflow: hidden;
    box-shadow: 0 10px 28px rgba(0,0,0,.35);
  }
  .card--back { top: 100px; background: var(--card-dark); }
  .card--front { top: 480px; background: var(--card-dark); }
  .card__art { position: absolute; inset: 0; width: 100%; height: 100%; }

  .brand { position: absolute; text-align: center; color: var(--ink); }
  .brand__name {
    font-family: "Questrial", Arial, sans-serif;
    font-weight: 400;
    line-height: 1;
    white-space: nowrap;
  }
  .brand__web {
    font-family: "Open Sans", Arial, sans-serif;
    font-weight: 700;
    margin-top: 4px;
  }
  .card--back .brand { left: 0; width: 560px; top: 118px; }
  .card--back .brand__name { font-size: 30px; }
  .card--back .brand__web { font-size: 9px; }
  .card--front .brand { left: 0; width: 245px; top: 138px; }
  .card--front .brand__name { font-size: 30px; }
  .card--front .brand__web { font-size: 10px; }

  .person { position: absolute; left: 292px; top: 70px; color: var(--paper-text); }
  .person__name { font-size: 23px; font-weight: 400; letter-spacing: .3px; }
  .person__title { font-size: 12px; margin: 2px 0 0 4px; }
  .person__rule { width: 142px; height: 2px; background: var(--paper-text); margin: 8px 0 0 2px; }

  .contacts { position: absolute; left: 292px; top: 186px; list-style: none; color: var(--paper-text); }
  .contacts li { display: flex; align-items: center; height: 26px; font-size: 14px; }
  .contacts svg { width: 18px; height: 18px; margin-right: 9px; flex: none; }
</style>
</head>
<body>

<section class="card card--back" aria-label="Card back">
  <svg class="card__art" viewBox="0 0 560 320" aria-hidden="true">
    <polygon points="0,112 560,8 560,172 0,282" fill="var(--card-white)"/>
    <polygon points="0,98 380,28 380,41 0,112" fill="var(--brand-blue)"/>
    <polygon points="210,241 560,172 560,188 210,254" fill="var(--brand-blue)"/>
  </svg>
  <div class="brand">
    <div class="brand__name">Vemtra Group</div>
    <div class="brand__web">www.vemtragroup.com</div>
  </div>
</section>

<section class="card card--front" aria-label="Card front">
  <svg class="card__art" viewBox="0 0 560 320" aria-hidden="true">
    <defs>
      <linearGradient id="stripe-fade" x1="0" x2="1">
        <stop offset="0" stop-color="var(--brand-blue-light)"/>
        <stop offset="1" stop-color="var(--brand-blue)"/>
      </linearGradient>
    </defs>
    <rect x="0" y="0" width="245" height="320" fill="var(--card-white)"/>
    <rect x="245" y="0" width="22" height="320" fill="url(#stripe-fade)"/>
  </svg>
  <div class="brand">
    <div class="brand__name">Vemtra Group</div>
    <div class="brand__web">www.vemtragroup.com</div>
  </div>

  <div class="person">
    <div class="person__name">Your Name Here</div>
    <div class="person__title">Tittle here</div>
    <div class="person__rule"></div>
  </div>

  <ul class="contacts">
    <li>
      <svg viewBox="0 0 20 20" aria-hidden="true"><circle cx="10" cy="10" r="9" fill="none" stroke="currentColor" stroke-width="1.3"/><rect x="7" y="4.5" width="6" height="11" rx="1" fill="none" stroke="currentColor" stroke-width="1.3"/><circle cx="10" cy="13.5" r=".7" fill="currentColor"/></svg>
      Cellphone
    </li>
    <li>
      <svg viewBox="0 0 20 20" aria-hidden="true"><circle cx="10" cy="10" r="9" fill="none" stroke="currentColor" stroke-width="1.3"/><path d="M6.5 5.5l2 0 1 2.5-1.3 1a6 6 0 0 0 2.8 2.8l1-1.3 2.5 1v2a1 1 0 0 1-1 1A8 8 0 0 1 5.5 6.5a1 1 0 0 1 1-1z" fill="currentColor"/></svg>
      Company phone
    </li>
    <li>
      <svg viewBox="0 0 20 20" aria-hidden="true"><circle cx="10" cy="10" r="9" fill="none" stroke="currentColor" stroke-width="1.3"/><rect x="5" y="6.5" width="10" height="7" fill="currentColor"/><path d="M5 6.5l5 4 5-4" fill="none" stroke="var(--card-dark)" stroke-width="1"/></svg>
      youremail@mailbox.com
    </li>
    <li>
      <svg viewBox="0 0 20 20" aria-hidden="true"><circle cx="10" cy="10" r="9" fill="none" stroke="currentColor" stroke-width="1.3"/><circle cx="10" cy="10" r="5" fill="none" stroke="currentColor" stroke-width="1.2"/><path d="M5 10h10M10 5c-2.5 3-2.5 7 0 10M10 5c2.5 3 2.5 7 0 10" fill="none" stroke="currentColor" stroke-width="1"/></svg>
      www.yourwebsite.com
    </li>
  </ul>
</section>

</body>
</html>
```